Website design and Setup for Real Estate Firm and Going Live

We are a commercial real estate investment firm and are looking for a 6 page website which is informational only. Some text and graphics on each page. We would want the designer to code and launch the website. This website needs to be corporate looking as well as innovative. We are setting up the website on webnook.

The first page will be a home page with generic commercial real estate look with a link to the following 5 pages on page 1. So page one (the Home Page should have a commercial real estate look with the text linking to the following pages. Page 2 "About Us" with 3 paragraphs describing our firm. Page 3 "Our Platform" with another few paragraphs on due diligence, acquisitions, financing, and management.

Page 4 is "Our Team" highlighting several manager profiles. Page 5 is our "investment Portfolio portal" which will be password protected so not a lot of text, only general graphics and anyone viewing the site casually won't get into the backend, Page 6 is the contact us page. All of the content will be uploaded shortly.

The project includes setting up hyperlinks in the website as well rotating images etc and a final complete live online product. We do not expect to pay for any stock images.

Target Market(s)

Investors, Real Estate Professionals, Brokerages

Industry/Entity Type

Real Estate

Coding

Coded - Design and coding required

Number of Pages Required

5+ page

Requirements
Must have
• Corporate cutting edge design, suitable for a financial corporation.

```html
<!DOCTYPE html>
<html lang="en">
<head>
<meta charset="utf-8">
<title>Meridian Crest — Real Estate Investment Firm</title>
<link href="https://fonts.googleapis.com/css2?family=Montserrat:wght@300;400;500;600;700&display=swap" rel="stylesheet">
<style>
:root{
  --ink:#222630;
  --slate:#3f434b;
  --slate-dark:#34373e;
  --grey:#8d9096;
  --grey-light:#c4c7cc;
  --mist:#eef0f3;
  --white:#ffffff;
  --sky:#6f9cc8;
  --sky-deep:#2e5c8f;
  --line:#d6d8dc;
}
*{box-sizing:border-box;margin:0;padding:0}
html,body{width:1200px;height:4079px;overflow:hidden}
body{font-family:'Montserrat',sans-serif;color:var(--ink);background:var(--white);position:relative}
.abs{position:absolute}
a{color:inherit;text-decoration:none}

/* header */
.site-header{left:0;top:0;width:1200px;height:123px;background:var(--white)}
.brand{left:92px;top:58px;width:210px;text-align:center}
.brand-mark{display:inline-block;width:34px;height:34px;border:3px solid var(--grey);margin-bottom:6px}
.brand-name{font-size:22px;font-weight:400;color:var(--grey);letter-spacing:.5px}
.brand-sub{font-size:7px;letter-spacing:3px;color:var(--grey-light);margin-top:2px}
.brand-top{top:0}
.main-nav{left:343px;top:76px;display:flex;gap:37px;font-size:11.5px;font-weight:500;letter-spacing:.6px;color:var(--grey)}
.main-nav .active{color:var(--ink);font-weight:600;position:relative}
.main-nav .active::after{content:"";position:absolute;left:-3px;right:-3px;top:44px;height:3px;background:var(--line)}
.call-btn{left:825px;top:0;width:256px;height:37px;background:var(--grey);color:var(--white);font-size:12.5px;font-weight:600;letter-spacing:.8px;display:flex;align-items:center;justify-content:center;gap:8px}

/* hero */
.hero{left:0;top:123px;width:1200px;height:664px;background:linear-gradient(160deg,#4d6a8c 0%,#8aa4bf 30%,#c6d3e0 48%,#6a6f77 70%,#8c6b48 100%);clip-path:polygon(0 0,100% 0,100% 600px,0 664px)}
.hero-edge{left:545px;top:728px;width:655px;height:45px;background:var(--grey-light);clip-path:polygon(0 100%,100% 0,100% 30%,0 100%)}
.hero-copy{left:124px;top:327px;color:var(--white)}
.hero-copy .kicker{font-size:38px;font-weight:300;letter-spacing:1px}
.hero-copy h1{font-size:47px;font-weight:700;letter-spacing:.5px;line-height:1.1}
.hero-copy .tag{font-size:23px;font-weight:400;letter-spacing:3px;margin-top:12px}
.hero-actions{display:flex;gap:10px;margin-top:24px}
.btn-solid{width:180px;height:44px;background:var(--grey-light);color:var(--white);font-size:13px;font-weight:600;letter-spacing:1px;display:flex;align-items:center;justify-content:center}
.btn-light{width:180px;height:44px;background:var(--white);color:var(--ink);font-size:13px;font-weight:600;letter-spacing:1px;display:flex;align-items:center;justify-content:center}

/* section titles */
.section-title{width:1200px;left:0;text-align:center;font-size:29px;letter-spacing:.8px;font-weight:400}
.section-title b{font-weight:700}
.rule{height:3px;background:var(--grey-light);width:50px}

/* approach */
.dots{left:112px;top:935px;width:148px;height:148px;background-image:radial-gradient(var(--grey-light) 1.2px,transparent 1.4px);background-size:6px 6px}
.approach-card{top:957px;width:228px;height:248px;background:var(--white);border:1.5px solid var(--line);text-align:center;padding:30px 20px 0}
.approach-card.featured{top:936px;height:290px;background:var(--slate);color:var(--white);border:none;padding-top:48px}
.approach-card svg{width:48px;height:48px}
.approach-card h3{font-size:15px;font-weight:600;margin:18px 0 8px}
.approach-card p{font-size:11px;line-height:1.6;color:var(--grey)}
.approach-card.featured p{color:#dfe1e4}
.mini-btn{margin:16px auto 0;width:126px;height:26px;background:var(--grey);color:var(--white);font-size:9px;letter-spacing:1px;display:flex;align-items:center;justify-content:center}

/* company */
.company-band{left:0;top:1275px;width:1200px;height:633px;background:linear-gradient(90deg,#f7f8fa,var(--mist));clip-path:polygon(0 65px,100% 0,100% 100%,0 100%)}
.company-strip{left:0;top:1300px;width:565px;height:50px;background:var(--grey-light);clip-path:polygon(0 40px,100% 0,100% 12px,0 52px)}
.company-photo{left:0;top:1340px;width:800px;height:568px;background:linear-gradient(140deg,#b8d3ec 0%,#5e8fc0 40%,#2f5f90 65%,#e6ecf2 100%);-webkit-mask-image:linear-gradient(90deg,#000 60%,transparent 100%);mask-image:linear-gradient(90deg,#000 60%,transparent 100%)}
.company-copy{left:642px;top:1450px;width:445px}
.company-copy h2{font-size:32px;font-weight:400;letter-spacing:.5px}
.company-copy h2 b{font-weight:700}
.company-copy .rule{background:var(--ink);width:60px;margin:6px 0 22px}
.company-copy p{font-size:13.5px;line-height:1.72;color:var(--slate);text-align:justify;margin-bottom:14px}
.btn-outline{display:flex;align-items:center;justify-content:center;border:2px solid var(--slate);font-size:13px;font-weight:600;letter-spacing:1px;color:var(--slate)}

/* portfolio */
.portfolio{left:0;top:1908px;width:1200px;height:560px;background:linear-gradient(180deg,var(--slate) 0%,#4a4e56 60%,#6b7078 100%);clip-path:polygon(0 0,100% 0,100% 100%,0 100%)}
.portfolio-skyline{left:0;top:2100px;width:1200px;height:280px;background:linear-gradient(90deg,rgba(120,125,132,.55),rgba(80,84,92,.1) 40%,rgba(80,84,92,.1) 60%,rgba(130,135,142,.55));clip-path:polygon(0 0,100% 0,100% 100%,0 100%)}
.portfolio-title{top:1975px;color:var(--white)}
.portfolio-lead{left:300px;width:600px;top:2040px;text-align:center;font-size:14.5px;line-height:1.5;color:var(--grey-light)}
.portfolio-card{top:2128px;width:449px;height:317px;color:var(--white);text-align:center;display:flex;flex-direction:column;justify-content:flex-end;padding-bottom:26px}
.portfolio-card h3{font-size:15px;font-weight:600;margin-bottom:4px}
.portfolio-card p{font-size:14px;line-height:1.2}
.photo-a{background:linear-gradient(150deg,#dce7f1 0%,#5d89b6 45%,#2a4f7a 80%,#4a5564 100%)}
.photo-b{background:linear-gradient(200deg,#c7d8ea 0%,#5b86b2 40%,#244a74 75%,#4a5564 100%)}

/* team */
.team{left:0;top:2470px;width:1200px;height:608px;background:linear-gradient(180deg,#f6f7f9 0%,#eceef1 60%,#d8dbe0 100%)}
.team-frame{left:118px;top:2562px;width:640px;height:430px;border:5px solid var(--grey)}
.team-copy{left:193px;top:2636px;width:360px}
.kicker-small{font-size:13px;letter-spacing:2px;color:var(--grey)}
.team-copy h2{font-size:36px;font-weight:400;color:var(--slate);letter-spacing:.5px;margin:3px 0 8px}
.team-copy h2 b{font-weight:700}
.team-copy .rule{background:var(--grey-light);width:62px;margin-bottom:24px}
.team-copy p{font-size:13.5px;line-height:1.7;color:var(--slate);text-align:justify}
.team-photo{left:570px;top:2500px;width:540px;height:578px;background:linear-gradient(90deg,rgba(110,114,120,.0) 0%,#8b8f96 20%,#b4875d 70%,rgba(236,238,241,0) 100%);border-radius:200px 200px 0 0}

/* contact */
.contact-ring{left:142px;top:3150px;width:460px;height:460px;border-radius:50%;background:linear-gradient(135deg,#6b87a8,#3f434b 80%)}
.contact-photo{left:160px;top:3168px;width:424px;height:424px;border-radius:50%;border:10px solid var(--white);background:radial-gradient(circle at 45% 55%,#6fb2ef 0%,#2c5fa3 40%,#0e2342 80%)}
.contact-copy{left:640px;top:3230px;width:400px}
.contact-copy h2{font-size:36px;font-weight:400;color:var(--slate);letter-spacing:.5px;margin:4px 0 8px}
.contact-copy h2 b{font-weight:700}
.contact-copy .rule{background:var(--grey-light);width:62px;margin-bottom:24px}
.contact-copy p{font-size:13.5px;line-height:1.7;color:var(--slate);text-align:justify}

/* footer */
.footer-strip{left:0;top:3640px;width:660px;height:70px;background:#d7e1ee;clip-path:polygon(0 62px,100% 20px,100% 32px,0 74px)}
.site-footer{left:0;top:3615px;width:1200px;height:464px;background:var(--slate);clip-path:polygon(0 92px,100% 0,100% 100%,0 100%)}
.footer-brand{left:145px;top:3748px;width:240px;text-align:center;color:var(--white)}
.footer-brand .brand-mark{border-color:var(--white)}
.footer-brand .brand-name{color:var(--white);font-size:23px}
.footer-brand .brand-sub{color:var(--white)}
.footer-brand p{font-size:10.5px;line-height:1.6;color:var(--grey-light);margin-top:10px}
.footer-col{top:3715px;height:195px;border-left:1px solid #55595f;padding:30px 0 0 36px}
.footer-col h4{font-size:13px;font-weight:600;color:var(--white);margin-bottom:16px;position:relative}
.footer-col h4::before{content:"";position:absolute;left:-38px;top:-2px;width:3px;height:20px;background:var(--grey-light)}
.footer-col li{list-style:none;font-size:13px;color:var(--grey-light);margin-bottom:10px}
.footer-col.small li{font-size:11.5px;margin-bottom:12px}
.social{display:flex;gap:7px}
.social span{width:28px;height:28px;border-radius:50%;background:var(--white)}
.copyright{left:0;top:4008px;width:1200px;height:71px;background:var(--slate-dark);border-top:1px solid #55595f;text-align:center;font-size:11px;color:var(--grey-light);padding-top:26px}
</style>
</head>
<body>

<header class="site-header abs">
  <div class="brand abs" style="top:4px">
    <span class="brand-mark"></span>
    <div class="brand-name">MERIDIAN CREST</div>
    <div class="brand-sub">REAL ESTATE</div>
  </div>
  <nav class="main-nav abs">
    <a class="active" href="#">OUR COMPANY</a>
    <a href="#">INVESTMENT APPRAOCH</a>
    <a href="#">EXECUTIVE TEAM</a>
    <a href="#">INVESTMENT PORTFOLIO</a>
    <a href="#">CONTACT</a>
  </nav>
  <a class="call-btn abs" href="#">
    <svg width="16" height="16" viewBox="0 0 24 24" fill="none" stroke="#fff" stroke-width="2"><path d="M5 3h4l2 5-3 2a11 11 0 0 0 6 6l2-3 5 2v4a2 2 0 0 1-2 2A17 17 0 0 1 3 5a2 2 0 0 1 2-2z"/></svg>
    CALL US (+100) 555 0199
  </a>
</header>

<section class="hero abs" role="img" aria-label="Upward view of city skyscrapers against a blue sky"></section>
<div class="hero-edge abs"></div>
<div class="hero-copy abs">
  <div class="kicker">WELCOME TO</div>
  <h1>MERIDIAN CREST</h1>
  <div class="tag">REAL ESTATE INVESTMENT FIRM</div>
  <div class="hero-actions">
    <a class="btn-solid" href="#">LEARN MORE</a>
    <a class="btn-light" href="#">CONTACT US</a>
  </div>
</div>

<h2 class="section-title abs" style="top:852px"><b>INVESTMENT</b> APPROACH</h2>
<div class="rule abs" style="left:575px;top:900px"></div>

<div class="dots abs"></div>
<article class="approach-card abs" style="left:130px">
  <svg viewBox="0 0 48 48" fill="none" stroke="#3f434b" stroke-width="1.6"><circle cx="24" cy="14" r="9"/><path d="M24 9v10M21 11h5a2 2 0 0 1 0 4h-4a2 2 0 0 0 0 4h5"/><path d="M6 34l8-6h8l6 3h-9M6 40l10-2 16-7 8-3"/></svg>
  <h3>ACQUISITIONS</h3>
  <p>Lorem ipsum dolor sit amet, consectetur adipiscing elit, sed do eiusmod tempor incididunt ut labore et dolore magna</p>
</article>
<article class="approach-card featured abs" style="left:367px">
  <svg viewBox="0 0 48 48" fill="none" stroke="#fff" stroke-width="1.6"><path d="M14 40v-8a14 14 0 1 1 20-12l3 6h-3v6h-6v8"/><circle cx="22" cy="20" r="5"/><path d="M22 12v3M22 25v3M14 20h3M27 20h3"/></svg>
  <h3>DUE DILIGENCE</h3>
  <p>Lorem ipsum dolor sit amet, consectetur adipiscing elit, sed do eiusmod tempor incididu</p>
  <a class="mini-btn" href="#">LEARN MORE</a>
</article>
<article class="approach-card abs" style="left:605px">
  <svg viewBox="0 0 48 48" fill="none" stroke="#3f434b" stroke-width="1.6"><path d="M6 42h36M10 42V30h5v12M19 42V24h5v18M28 42V28h5v14M37 42V20h5v22"/><path d="M8 24l10-8 8 4 12-10"/><circle cx="38" cy="10" r="4"/></svg>
  <h3>FINANCING</h3>
  <p>Lorem ipsum dolor sit amet, consectetur adipiscing elit, sed do eiusmod tempor incididunt ut labore et dolore magna</p>
</article>
<article class="approach-card abs" style="left:840px">
  <svg viewBox="0 0 48 48" fill="none" stroke="#3f434b" stroke-width="1.6"><circle cx="20" cy="24" r="6"/><path d="M20 12v4M20 32v4M8 24h4M28 24h4M12 16l3 3M25 29l3 3M12 32l3-3M25 19l3-3"/><circle cx="34" cy="12" r="4"/><path d="M34 5v3M34 16v3M27 12h3M38 12h3"/></svg>
  <h3>MANAGEMENT</h3>
  <p>Lorem ipsum dolor sit amet, consectetur adipiscing elit, sed do eiusmod tempor incididunt ut labore et dolore magna</p>
</article>

<section class="company-band abs"></section>
<div class="company-strip abs"></div>
<div class="company-photo abs" role="img" aria-label="Modern glass office building with trees at its base"></div>
<div class="company-copy abs">
  <h2>OUR <b>COMPANY</b></h2>
  <div class="rule"></div>
  <p>Lorem ipsum dolor sit amet, consectetur adipiscing elit, sed do eiusmod tempor incididunt ut labore et dolore magna aliqua.</p>
  <p>Ut enim ad minim veniam, quis nostrud exercitation ullamco laboris nisi ut aliquip ex ea commodo consequat. Duis aute irure dolor in reprehenderit in voluptate velit esse cillum dolore eu fugiat nulla pariatur. Excepteur sint occaecat cupidatasunt</p>
  <a class="btn-outline" href="#" style="width:170px;height:46px;margin-top:12px">LEARN MORE</a>
</div>

<section class="portfolio abs"></section>
<div class="portfolio-skyline abs" role="img" aria-label="Faded city skyline behind the portfolio cards"></div>
<h2 class="section-title portfolio-title abs"><b>INVESTMENT</b> PORTFOLIO</h2>
<div class="rule abs" style="left:582px;top:2025px;background:var(--white)"></div>
<p class="portfolio-lead abs">Lorem ipsum dolor sit amet, consectetur adipiscing elit, sed do eiusmod tempor incididunt ut labore et dolore magna aliqua</p>
<a class="portfolio-card photo-a abs" style="left:156px" href="#" role="img" aria-label="Glass office towers viewed from below">
  <h3>SED UTPERSPICIATIS</h3>
  <p>sit amet, consectetur adipiscing elit, sed<br>do eiusmod tempor incididunt</p>
</a>
<a class="portfolio-card photo-b abs" style="left:615px" href="#" role="img" aria-label="Skyscrapers reaching into a cloudy sky">
  <h3>NEQUE PORRO QUISQUAM</h3>
  <p>sit amet, consectetur adipiscing elit, sed<br>do eiusmod tempor incididunt</p>
</a>

<section class="team abs"></section>
<div class="team-frame abs"></div>
<div class="team-copy abs">
  <div class="kicker-small">WHO WE ARE</div>
  <h2>MEET <b>THE TEAM</b></h2>
  <div class="rule"></div>
  <p>Lorem ipsum dolor sit amet, consectetur adipiscing elit, sed do eiusmod tempor incididunt ut labore et dolore magna aliqua. Ut enim ad minim veniam, quis nostrud exercitation ullamco laboris nisi ut aliquip</p>
  <a class="btn-outline" href="#" style="width:170px;height:46px;margin-top:36px">LEARN MORE</a>
</div>
<div class="team-photo abs" role="img" aria-label="Two smiling business people standing back to back with arms crossed"></div>

<div class="contact-ring abs"></div>
<div class="contact-photo abs" role="img" aria-label="Businessman holding a tablet with a glowing city network overlay"></div>
<div class="contact-copy abs">
  <div class="kicker-small">GET IN TOUCH WITH US</div>
  <h2>CONTACT <b>US</b></h2>
  <div class="rule"></div>
  <p>Lorem ipsum dolor sit amet, consectetur adipiscing elit, sed do eiusmod tempor incididunt ut labore et dolore magna aliqua. Ut enim ad minim veniam, quis nostrud exercitation ullamco laboris nisi ut aliquip</p>
  <a class="btn-outline" href="#" style="width:152px;height:40px;margin-top:36px;font-size:12px">CONTACT US</a>
</div>

<div class="footer-strip abs"></div>
<footer class="site-footer abs"></footer>
<div class="footer-brand abs">
  <span class="brand-mark"></span>
  <div class="brand-name">MERIDIAN CREST</div>
  <div class="brand-sub">REAL ESTATE</div>
  <p>Lorem ipsum dolor sit amet, consectetur<br>adipiscing elit, sed do eiusmod t</p>
</div>
<div class="footer-col abs" style="left:463px;width:235px">
  <h4>NAVIGATION</h4>
  <ul><li>Our Company</li><li>Investment Approach</li><li>Team</li><li>Investment Portofolio</li></ul>
</div>
<div class="footer-col small abs" style="left:697px;width:200px">
  <h4>LINKS</h4>
  <ul><li>Terms &amp; Condition</li><li>Privacy Policy</li><li>Contct Us</li></ul>
</div>
<div class="footer-col abs" style="left:897px;width:200px">
  <h4>FOLLOW US</h4>
  <div class="social"><span></span><span></span><span></span></div>
</div>
<div class="copyright abs">© 2021 Meridian Crest &nbsp;| All Rights Reserved</div>

</body>
</html>
```